Lantern Airfields Homepage Design Update

here's the current site - http://lanternairfields.example/

client is not happy with overall look.

keeping the same info - intro text, headlines, featured media excepts and general navigation options - can you come up with a nicer, slicker look for this homepage?

UPDATE: since it was asked by designer.. the general layout doesnt have to be the same. its not required to have a big image, with text below that and then smaller images/text below that. as long as we have the same content on the page, it can organized and designed in any way,

client like big images, so one way or the other, keep that... but feel free to reorganize content, explore different ways of framing it, and/or anything else. make this homepage pop!

for the designer that wins this, we'll start an additional project to update the interior.

let me know if any questions..

thanks!

marcus

Target Market(s)

aviation industry professionals, local governments, general public

Number of Pages Required

1 page

Font styles to use
Sans Serif

Requirements
Must have
• big image somewhere. same content as on current site, just designed differently.

```html
<!DOCTYPE html>
<html lang="en">
<head>
<meta charset="utf-8">
<title>Lantern Airfields</title>
<link rel="stylesheet" href="https://fonts.googleapis.com/css2?family=Ubuntu:wght@300;400;500&display=swap">
<style>
:root{
  --navy:#2f2d4f;
  --navy-deep:#28263f;
  --green:#7dc01c;
  --ink:#33324a;
  --muted:#b9b7d0;
  --light:#f5f5f5;
  --white:#ffffff;
}
*{box-sizing:border-box;margin:0;padding:0}
html,body{width:1200px;height:2293px;overflow:hidden}
body{font-family:'Ubuntu',sans-serif;background:var(--white);color:var(--ink);position:relative}
a{color:inherit;text-decoration:none}

.site-header{position:absolute;left:0;top:0;width:1200px;height:83px;background:var(--white)}
.brand{position:absolute;left:197px;top:24px;display:flex;align-items:center;gap:10px;font-size:24px;font-weight:300;color:var(--ink)}
.brand-mark{width:14px;height:14px;border-radius:50%;background:var(--ink)}
.main-nav{position:absolute;top:34px;left:0;width:1200px;font-size:15px;color:var(--ink)}
.main-nav a{position:absolute;white-space:nowrap}
.nav-active{position:absolute;left:454px;top:83px;width:64px;height:4px;background:var(--green)}

.hero{position:absolute;left:0;top:83px;width:1200px;height:535px;
  background:linear-gradient(180deg,rgba(40,35,40,.35) 0%,rgba(0,0,0,0) 40%,rgba(30,25,20,.55) 100%),
  linear-gradient(100deg,#4d4a4f 0%,#9b8a6a 30%,#e1a63a 60%,#f0b63a 78%,#b77a24 100%)}
.hero-copy{position:absolute;left:197px;top:205px;color:var(--white)}
.hero-title{font-size:30px;font-weight:400;line-height:36px}
.hero-sub{font-size:18px;font-weight:400;margin-top:2px}
.btn{position:absolute;left:197px;top:321px;width:126px;height:33px;background:var(--green);color:var(--white);font-size:17px;line-height:33px;text-align:center}
.dots{position:absolute;left:197px;top:387px;display:flex;gap:5px}
.dots span{width:7px;height:7px;border-radius:50%;background:var(--white)}
.dots span:first-child{background:#333}

.intro{position:absolute;left:0;top:618px;width:1200px;height:390px;background:var(--light)}
.intro-panel{position:absolute;left:0;top:0;width:518px;height:390px;background:var(--navy)}
.intro-title{position:absolute;left:197px;top:80px;width:300px;font-size:40px;line-height:39px;font-weight:400;color:var(--green)}
.intro-text{position:absolute;left:534px;top:79px;width:480px;font-size:18.5px;line-height:31px;font-weight:300;color:var(--ink)}
.intro-text p+p{margin-top:15px}

.services{position:absolute;left:0;top:1008px;width:1200px;height:573px;
  background:linear-gradient(180deg,#c9a7b3 0%,#8f7f9b 35%,#6b6580 65%,#c9a59a 100%)}
.section-title{position:absolute;width:1200px;text-align:center;font-size:29px;font-weight:400}
.services .section-title{top:55px;color:var(--green)}
.service-grid{position:absolute;left:197px;top:108px;width:806px;height:355px}
.service{position:absolute;background:var(--navy);border-right:1px solid #3d3b5e;border-bottom:1px solid #3d3b5e;padding:46px 0 0 43px}
.service::before{content:"";position:absolute;left:22px;top:52px;width:6px;height:6px;border-top:2px solid var(--white);border-right:2px solid var(--white);transform:rotate(45deg)}
.service h3{font-size:15px;font-weight:400;line-height:20px;color:var(--green)}
.service p{margin-top:12px;font-size:10px;line-height:15.5px;color:var(--muted);font-weight:300;width:205px}
.service .more{color:var(--green);font-style:italic;font-weight:500}
.service-highlight{background:var(--green)}
.service-highlight h3{color:var(--white);font-size:16px;line-height:21px;width:200px}
.service-highlight .more{color:var(--navy);font-size:10px}

.news{position:absolute;left:0;top:1581px;width:1200px;height:364px}
.news .section-title{top:28px;color:var(--ink);font-size:31px}
.news-arrow{position:absolute;top:44px;width:9px;height:9px;border-top:2px solid var(--ink);border-right:2px solid var(--ink)}
.news-rule{position:absolute;left:197px;top:81px;width:806px;height:1px;background:#ddd}
.news-card{position:absolute;top:115px;width:252px}
.news-photo{height:156px;position:relative}
.date-badge{position:absolute;left:11px;top:0;width:62px;height:68px;background:var(--green);color:var(--white);font-size:11px;font-weight:500;line-height:12px;padding:8px 0 0 16px;clip-path:polygon(0 0,100% 0,100% 100%,50% 85%,0 100%)}
.news-caption{margin-top:10px;font-size:12px;line-height:20px;color:var(--ink)}

.site-footer{position:absolute;left:0;top:1945px;width:1200px;height:348px;background:var(--navy);color:var(--white)}
.footer-col{position:absolute;top:40px;font-size:14px}
.footer-col h4{color:var(--green);font-size:13.5px;font-weight:500;margin-bottom:36px}
.footer-col li{list-style:none;line-height:26px}
.contact p{line-height:21px}
.social-dot{position:absolute;left:976px;width:27px;height:27px;border-radius:50%;background:var(--green)}
.footer-bottom{position:absolute;left:0;top:295px;width:1200px;height:53px;border-top:1px solid #3d3b5e;background:var(--navy-deep);text-align:center;font-size:13px;line-height:52px}
</style>
</head>
<body>

<header class="site-header">
  <a class="brand" href="#"><span class="brand-mark"></span>Lantern Airfields</a>
  <nav class="main-nav">
    <a style="left:469px">Home</a>
    <a style="left:533px">About</a>
    <a style="left:598px">Services</a>
    <a style="left:674px">Airports</a>
    <a style="left:751px">News &amp; Media</a>
    <a style="left:863px">Contact</a>
    <a style="left:937px">Employees</a>
  </nav>
  <span class="nav-active"></span>
</header>

<section class="hero" role="img" aria-label="Passenger jet on the apron at sunset under a golden sky">
  <div class="hero-copy">
    <h1 class="hero-title">Bringing private, free<br>enterprise business practices</h1>
    <p class="hero-sub">To airports throughout the U.S.</p>
  </div>
  <a class="btn" href="#">Learn More</a>
  <div class="dots"><span></span><span></span><span></span><span></span><span></span></div>
</section>

<section class="intro">
  <div class="intro-panel"><h2 class="intro-title">We develop P3 airport opportunities within the U.S. market</h2></div>
  <div class="intro-text">
    <p>Lantern Airfields is focused on opportunities to invest, develop and manage both general aviation and commercial service airports in key U.S. markets. A subsidiary of Lantern Capital Partners, a private equity firm that exclusively invests in the Aerospace &amp; Transportation sectors, Lantern has the resources available to invest and finance transactions.</p>
    <p>Lantern maintains offices in New York, Dublin and Atlanta.</p>
  </div>
</section>

<section class="services" role="img" aria-label="Blurred airport terminal window with a traveller silhouetted against the evening sky">
  <h2 class="section-title">Our Services</h2>
  <div class="service-grid">
    <div class="service" style="left:0;top:0;width:265px;height:178px">
      <h3>Private Capital for<br>development of P3 projects</h3>
      <p>Lorem Ipsum is simply dummy text of the printing and typesetting industry. Lorem Ipsum has been the industry's standard dummy text ever since the 1500s <span class="more">Read More &gt;&gt;</span></p>
    </div>
    <div class="service" style="left:265px;top:0;width:265px;height:178px">
      <h3>Sales and marketing<br>responsibility.</h3>
      <p>Lorem Ipsum is simply dummy text of the printing and typesetting industry. Lorem Ipsum has been the industry's standard dummy text ever since the 1500s <span class="more">Read More &gt;&gt;</span></p>
    </div>
    <div class="service" style="left:530px;top:0;width:276px;height:355px">
      <h3>Provide airport operation<br>services, if requested.</h3>
      <p style="margin-top:20px">Lorem Ipsum is simply dummy text of the printing and typesetting industry. Lorem Ipsum has been the industry's standard dummy text ever since the 1500s, when an unknown</p>
      <p style="margin-top:20px">Lorem Ipsum is simply dummy text of the printing and typesetting industry. Lorem Ipsum has been the industry's standard dummy text ever since the 1500s, when an unknown printer took a galley of type and scrambled it to make a type specimen book.<span class="more">Read More &gt;&gt;</span></p>
    </div>
    <div class="service" style="left:0;top:178px;width:265px;height:177px">
      <h3>Management of the overall P3.</h3>
      <p>Lorem Ipsum is simply dummy text of the printing and typesetting industry. Lorem Ipsum has been the industry's standard dummy text ever since the 1500s <span class="more">Read More &gt;&gt;</span></p>
    </div>
    <div class="service service-highlight" style="left:265px;top:178px;width:265px;height:177px;padding-top:30px">
      <h3>Coordination with the local authority and municipality for the development and engineering of an overall Master Plan for each development project <span class="more">Read More &gt;&gt;</span></h3>
    </div>
  </div>
</section>

<section class="news">
  <span class="news-arrow" style="left:199px;transform:rotate(-135deg)"></span>
  <h2 class="section-title">Featured News</h2>
  <span class="news-arrow" style="left:992px;transform:rotate(45deg)"></span>
  <div class="news-rule"></div>
  <article class="news-card" style="left:197px">
    <div class="news-photo" role="img" aria-label="Traveller walking through a dim terminal with a plane taking off outside" style="background:linear-gradient(180deg,#5a5a5e,#2c2c30)"><div class="date-badge">June<br>17th<br>2014</div></div>
    <p class="news-caption">New York Company Wants to Build Passenger Terminal at Cedar Field in Marlow, WA</p>
  </article>
  <article class="news-card" style="left:474px">
    <div class="news-photo" role="img" aria-label="Airliner landing over city lights at dusk" style="background:linear-gradient(180deg,#3a78b8,#8ab3d6 55%,#e0a060 80%,#3a3a5a)"><div class="date-badge">June<br>17th<br>2014</div></div>
    <p class="news-caption">New York Company Wants to Build Passenger Terminal at Cedar Field in Marlow, WA</p>
  </article>
  <article class="news-card" style="left:751px">
    <div class="news-photo" role="img" aria-label="Businessman checking his phone in a bright airport lounge" style="background:linear-gradient(90deg,#b9d1e0,#7d9fb8 55%,#2f3a55)"><div class="date-badge">June<br>17th<br>2014</div></div>
    <p class="news-caption">New York Company Wants to Build Passenger Terminal at Cedar Field in Marlow, WA</p>
  </article>
</section>

<footer class="site-footer">
  <div class="footer-col" style="left:197px">
    <h4>Quick Links</h4>
    <ul><li>Home</li><li>About</li><li>Services</li><li>Airports</li><li>News &amp; Media</li><li>Contact</li><li>Employees</li></ul>
  </div>
  <div class="footer-col" style="left:335px">
    <h4>Support Links</h4>
    <ul><li>Terms &amp; Conditions</li><li>Privacy Policy</li><li>Legal Notice</li></ul>
  </div>
  <div class="footer-col contact" style="left:543px">
    <h4>Contact Us</h4>
    <p>Corporate Office</p>
    <p style="margin-top:20px">410 Harbor Avenue, 12th Floor<br>New York, NY 10022<br>Main Phone Number: (212) 555-0148<br>Email: info@lanternairfields.example</p>
  </div>
  <div class="footer-col" style="left:820px">
    <h4>Connect With Us</h4>
    <ul><li>Friendbook</li><li style="margin-top:15px">Chirper</li></ul>
  </div>
  <span class="social-dot" style="top:88px"></span>
  <span class="social-dot" style="top:125px"></span>
  <div class="footer-bottom">© 2015 Company Name, All Rights Reserved</div>
</footer>

</body>
</html>
```